Tradeshow Booth Design

Clean background, some variance of kelly green in the colors - see image for text - maybe an image with people or nice modern homes...

Target Market(s)

Mortgage Professionals

Industry/Entity Type

Mortgage Lender

Font styles to use
Serif
Sans Serif

Colors
9bcb3c
cadf82

Requirements
Must have
• Logo, the words on the image

```html
<!DOCTYPE html>
<html lang="en">
<head>
<meta charset="utf-8">
<title>Meridian Home Loans – Tradeshow Backdrop</title>
<link href="https://fonts.googleapis.com/css2?family=Roboto+Condensed:wght@700&family=Josefin+Sans:wght@400&display=swap" rel="stylesheet">
<style>
  :root {
    --page-bg: #e6e6e6;
    --white-field: #f4f4f4;
    --forest: #234a2c;
    --forest-text: #25502f;
    --sage-light: #cad5bf;
    --sage-dark: #b3c0a5;
    --url-ink: #2b3a2e;
  }
  * { margin: 0; padding: 0; box-sizing: border-box; }
  html, body { width: 1200px; height: 960px; overflow: hidden; background: var(--page-bg); }

  .booth-panel {
    position: absolute;
    left: 30px;
    top: 75px;
    width: 1140px;
    height: 810px;
    background: var(--white-field);
    overflow: hidden;
  }
  .panel-art { position: absolute; inset: 0; width: 100%; height: 100%; }

  .brand-name {
    position: absolute;
    left: 0;
    right: 0;
    top: 96px;
    display: flex;
    justify-content: center;
    align-items: center;
    gap: 20px;
    padding-left: 60px;
    font-family: "Roboto Condensed", sans-serif;
    font-weight: 700;
    font-size: 72px;
    line-height: 1;
    color: var(--forest-text);
  }
  .brand-mark {
    width: 26px;
    height: 26px;
    background: var(--forest-text);
    flex: none;
  }

  .feature-list {
    position: absolute;
    list-style: none;
    font-family: "Roboto Condensed", sans-serif;
    font-weight: 700;
    font-size: 46px;
    line-height: 1;
    color: var(--forest-text);
  }
  .feature-list li {
    display: flex;
    align-items: center;
    height: 64px;
  }
  .feature-list .bullet {
    width: 22px;
    height: 22px;
    margin-right: 28px;
    flex: none;
  }
  .features-left { left: 170px; top: 440px; }
  .features-right { left: 724px; top: 440px; }

  .site-address {
    position: absolute;
    right: 42px;
    top: 770px;
    font-family: "Josefin Sans", sans-serif;
    font-size: 21px;
    letter-spacing: 4px;
    color: var(--url-ink);
  }
</style>
</head>
<body>
  <main class="booth-panel">
    <svg class="panel-art" viewBox="0 0 1140 810" preserveAspectRatio="none" aria-hidden="true">
      <defs>
        <linearGradient id="sageFill" x1="0" y1="0" x2="1" y2="0">
          <stop offset="0" stop-color="#b3c0a5"/>
          <stop offset="0.45" stop-color="#cad5bf"/>
          <stop offset="1" stop-color="#b3c0a5"/>
        </linearGradient>
        <linearGradient id="swooshFill" x1="0" y1="0" x2="1" y2="0">
          <stop offset="0" stop-color="#1f4428"/>
          <stop offset="0.55" stop-color="#2b5535"/>
          <stop offset="0.7" stop-color="#466b4e"/>
          <stop offset="1" stop-color="#234a2c"/>
        </linearGradient>
      </defs>
      <path class="sage-field" fill="url(#sageFill)"
        d="M0,170 C170,270 360,368 576,368 C760,368 950,262 1140,165 L1140,810 L0,810 Z"/>
      <path class="green-swoosh" fill="url(#swooshFill)"
        d="M0,40 C180,180 380,332 580,345 C690,352 780,330 840,305 C740,348 650,368 576,368 C360,368 170,270 0,170 Z"/>
    </svg>

    <h1 class="brand-name">
      <span class="brand-mark"></span>
      <span>MERIDIAN HOME LOANS</span>
    </h1>

    <ul class="feature-list features-left">
      <li><svg class="bullet" viewBox="-11 -11 22 22"><g stroke="var(--forest-text)" stroke-width="2.4" stroke-linecap="round"><line x1="0" y1="-10" x2="0" y2="10"/><line x1="-10" y1="0" x2="10" y2="0"/><line x1="-7" y1="-7" x2="7" y2="7"/><line x1="-7" y1="7" x2="7" y2="-7"/></g></svg>INNOVATIVE</li>
      <li><svg class="bullet" viewBox="-11 -11 22 22"><g stroke="var(--forest-text)" stroke-width="2.4" stroke-linecap="round"><line x1="0" y1="-10" x2="0" y2="10"/><line x1="-10" y1="0" x2="10" y2="0"/><line x1="-7" y1="-7" x2="7" y2="7"/><line x1="-7" y1="7" x2="7" y2="-7"/></g></svg>SOLUTIONS FOR</li>
      <li><svg class="bullet" viewBox="-11 -11 22 22"><g stroke="var(--forest-text)" stroke-width="2.4" stroke-linecap="round"><line x1="0" y1="-10" x2="0" y2="10"/><line x1="-10" y1="0" x2="10" y2="0"/><line x1="-7" y1="-7" x2="7" y2="7"/><line x1="-7" y1="7" x2="7" y2="-7"/></g></svg>NON-TRADITIONAL</li>
      <li><svg class="bullet" viewBox="-11 -11 22 22"><g stroke="var(--forest-text)" stroke-width="2.4" stroke-linecap="round"><line x1="0" y1="-10" x2="0" y2="10"/><line x1="-10" y1="0" x2="10" y2="0"/><line x1="-7" y1="-7" x2="7" y2="7"/><line x1="-7" y1="7" x2="7" y2="-7"/></g></svg>BORROWERS</li>
    </ul>

    <ul class="feature-list features-right">
      <li><svg class="bullet" viewBox="-11 -11 22 22"><g stroke="var(--forest-text)" stroke-width="2.4" stroke-linecap="round"><line x1="0" y1="-10" x2="0" y2="10"/><line x1="-10" y1="0" x2="10" y2="0"/><line x1="-7" y1="-7" x2="7" y2="7"/><line x1="-7" y1="7" x2="7" y2="-7"/></g></svg>FLEXIBLE</li>
      <li><svg class="bullet" viewBox="-11 -11 22 22"><g stroke="var(--forest-text)" stroke-width="2.4" stroke-linecap="round"><line x1="0" y1="-10" x2="0" y2="10"/><line x1="-10" y1="0" x2="10" y2="0"/><line x1="-7" y1="-7" x2="7" y2="7"/><line x1="-7" y1="7" x2="7" y2="-7"/></g></svg>GUIDELINES</li>
    </ul>

    <p class="site-address">www.meridianhomeloans.com</p>
  </main>
</body>
</html>
```